Dental Sleep Medicine Brochure

I am a dentist who practices dental sleep medicine with oral appliance therapy. I need a professional trifold brochure to give directly to patients as well as physicians. Since oral appliance therapy is little known, the brochure needs to be educational and informative. I am new in town, so I would also like it to provide some information about me, from a marketing standpoint.

Target Market(s)

Physicians and other referral sources.
Patients for education.

Industry/Entity Type

Dental

Requirements
Must have
• "Did You Know" - regular snorers have a 33% increased risk of cardiovascular disease. -Patients with Obstructive Sleep Apnea (OSA) are four times more likely to have a heart attack. -40-80% of stroke victims also suffer from OSA.
• How Does Snoring Indicate Obstructive Sleep Apnea? Snoring is often a precursor to something more serious called Obstructive Sleep Apnea. Snoring and OSA are similar respiratory sleep disorders. Snoring occurs when the air you breathe vibrates the tissues of the airway due to a blocked or narrowed airways (nose, mouth, or throat) OSA occurs when your breathing regularly sops or is slowed for 10 seconds or longer due to blocked or narrowed airways.
• Treatment Options: In addition to lifestyle changes such as good sleep hygiene, exercise and weight loss, there are 3 primary ways to treat snoring and sleep apnea: 1. CPAP (continuous positive airway pressure) 2. Surgery 3. Oral Appliance Therapy.
• Oral appliances can be used alone or in conjunction with other means of therapy such as continuous positive air pressure (CPAP). Determination of proper therapy can only be made by joint consultation of our office and your sleep physician.
• Oral appliances are indicated For patients with mild to moderate OSA who prefer OAs to Continuous Positive Airway Pressure (CPAP) and all cases where a patient is intolerant or refuses use of CPAP.
• How Do Oral Appliances Work?Oral Appliances are placed in the mouth and are worn much like an orthodontic appliance or sports mouth protector. They are worn during sleep to prevent the collapse of the tongue and soft tissues in the back of the throat so that the airway stays open during sleep. The appliances promote adequate air intake and help to provide normal sleep in people who snore and have sleep apnea.
• Your Experience: Upon diagnosis by a physician, Dr. Pemberly will thoroughly examine your teeth and mouth to confirm your oral health status, as well to ensure that you are dentally appropriate for an Oral Appliance. A series of impressions will then be taken and the proper FDA approved device will be fabricated. At the seating appointment, the appliance will be seated and checked for fit. Use and care instructions are given. There will then be a series of titration visits, which so that the optimal position of the appliance can be determined. Once this optimal position has been achieved, Dr. Pemberly will refer you back to your physician for a follow up sleep study. You should return for follow-up dental visits twice in the first year and annually thereafter.
• Do You Suffer From OSA? If you have OSA or display symptoms of OSA such as snoring, excessive daytime sleepiness, fatigue, and pauses in breathing while you sleep, it is essential that you seek the right treatment option.
• Do you snore (yes no)
• Do you have high blood pressure (yes no)
• Do you feel fatigued or excessively tired during he day? (yes no)
• Have you been told you choke or gasp during sleep? (yes no)
• Have you attempted any treatments for sleep disordered breathing? (yes no)
• If you answered yes to ANY of these questions, ask your physician about being evaluated further for risk of sleep disordered breathing.
• Why is Obstructive Sleep Apnea a problem? Your body is being robbed of the rest it needs to function properly during the day when you are constantly awoken throughout the night.
• OSA symptoms include:excessive daytime sleepiness, feeling exhausted after a normal night of sleep, headaches, depression.
• Symptoms that your bed partner is likely aware of: frequent episodes of obstructive breathing during sleep; snoring, gasps,choking or gurgling sounds; bruxism (tooth grinding)
• Long term symptoms: increased risk for high blood pressure and cardiovascular disease, sexual dysfunction, compromised immune system, irritability, learning and memory problems, poor mental and emotional health
• OSA is classified as mild, moderate, or severe, depending on the number of apnea (breathing stops) or hypopnea (breathing decreases) events per hour.
• Dr Pemberly attended the Halvorsen College of Oral and Dental Sciences, graduating at the top of her class while earning numerous awards along the way.
• She was then selected to attend an intensive General Practice Residency program at Brackenfield General Hospital where she trained under some of the top attendings in Oral Surgery, Pediatrics, Endodontics and Prosthodontics.
• Since then, she worked in a variety of private practice settings, most importantly, her own practice in the Princeton area of NJ, where she worked with many area sleep physicians to treat their CPAP intolerant patients with Oral appliance therapy. She has since relocated to the Northwest with her family, joining Quillmont Dental Center.
• Dr. Pemberly is a lifelong learner and dedicates countless hours to continuing education in all areas of dentistry. This allows her to stay on the cutting edge of dentistry and provide the best care available to her patients. She has gained extensive experience in the treatment of obstructive sleep apnea as well as all other phases of general dentistry. She is a member of the dental honors fraternity, Sigma Theta Rho, as well as the Guild of Family Dental Practice, Continental Dental Federation, National Council for Dental Sleep Medicine, and Tallmoor Valley and Orrin Basin Dental Societies.

```html
<!DOCTYPE html>
<html lang="en">
<head>
<meta charset="utf-8">
<title>Sleep Related Breathing Disorders – Dr. Pemberly</title>
<link href="https://fonts.googleapis.com/css2?family=Aldrich&family=Arimo:wght@400;700&display=swap" rel="stylesheet">
<style>
  :root {
    --navy-deep: #0b1f6e;
    --navy: #13329a;
    --royal: #1f4fc4;
    --gold: #f5a623;
    --gold-band: #d9a318;
    --gold-dark: #a77a0c;
    --white: #ffffff;
    --ring: #0e2a86;
  }
  * { margin: 0; padding: 0; box-sizing: border-box; }
  html, body { width: 1200px; height: 930px; overflow: hidden; background: var(--navy-deep); }
  .brochure-panel {
    position: relative;
    width: 1200px; height: 930px; overflow: hidden;
    background: radial-gradient(ellipse at 75% 70%, var(--royal) 0%, var(--navy) 45%, var(--navy-deep) 100%);
    font-family: "Arimo", Arial, sans-serif;
    color: var(--white);
  }
  .gold-waves { position: absolute; inset: 0; }
  .section-title {
    position: absolute; top: 18px;
    font-family: "Aldrich", sans-serif;
    font-size: 41px; font-weight: 400;
    color: var(--gold);
    letter-spacing: 0.5px;
  }
  .about-title { left: 20px; }
  .sleep-title { left: 413px; }
  .about-column {
    position: absolute; left: 20px; top: 117px; width: 356px;
    font-size: 17.5px; line-height: 24.4px; text-align: justify;
  }
  .about-column p { margin-bottom: 48px; }
  .about-column p:first-child { margin-bottom: 46px; }
  .sleep-column { position: absolute; left: 413px; top: 117px; width: 768px; }
  .callout {
    font-weight: 700; font-size: 16.5px; line-height: 22px;
    color: var(--gold); text-transform: uppercase;
    letter-spacing: 0.2px;
  }
  .body-text { font-size: 16.3px; line-height: 23.5px; text-align: justify; }
  .airway-diagram {
    position: absolute; left: 0; top: 66px; width: 464px; height: 130px;
    border-radius: 14px; background: linear-gradient(90deg, #f4f8fb, #e4eef5);
  }
  .intro-text { position: absolute; left: 0; top: 72px; width: 768px; }
  .intro-text .wrap-space { float: left; width: 472px; height: 130px; }
  .intro-text p { margin-bottom: 9px; }
  .therapy-callout { position: absolute; left: 0; top: 336px; width: 660px; }
  .appliance-intro { position: absolute; left: 0; top: 406px; width: 768px; }
  .appliance-options { position: absolute; left: 0; top: 514px; width: 488px; }
  .appliance-photo {
    position: absolute; left: 905px; top: 585px; width: 250px; height: 250px;
    border-radius: 50%;
    background: radial-gradient(circle at 50% 45%, #6d7a6a 0%, #2b3230 55%, #0c0f0f 100%);
    border: 9px solid var(--ring);
    box-shadow: 0 0 0 5px #dfe6f2;
  }
</style>
</head>
<body>
<main class="brochure-panel">
  <svg class="gold-waves" width="1200" height="930" viewBox="0 0 1200 930" aria-hidden="true">
    <path d="M0 752 C120 728 260 735 400 780 C520 820 640 900 700 930 L0 930 Z" fill="var(--gold-band)"/>
    <path d="M0 752 C120 728 260 735 400 780 C520 820 640 900 700 930" fill="none" stroke="var(--gold-dark)" stroke-width="3"/>
    <path d="M1200 548 C1150 630 1070 720 990 790 C930 845 890 895 870 930 L1200 930 Z" fill="var(--gold-band)"/>
    <path d="M1200 548 C1150 630 1070 720 990 790 C930 845 890 895 870 930" fill="none" stroke="var(--gold-dark)" stroke-width="3"/>
  </svg>

  <h1 class="section-title about-title">About Us</h1>
  <h1 class="section-title sleep-title">Sleep Related Breathing Disorders</h1>

  <section class="about-column">
    <p>- Dr. Pemberly is a lifelong learner and dedicates countless hours to continuing education in all areas of dentistry. This allows her to stay on the cutting edge of dentistry and provide the best care available to her patients.</p>
    <p>She has gained extensive experience in the treatment of obstructive sleep apnea as well as all other phases of general dentistry.</p>
    <p>She is a member of the dental honors fraternity, Sigma Theta Rho, as well as the Guild of Family Dental Practice, Continental Dental Federation, National Council for Dental Sleep Medicine, and Tallmoor Valley and Orrin Basin Dental Societies.</p>
  </section>

  <section class="sleep-column">
    <p class="callout">It has been estimated that as many as 40% of the US adult population suffer from some form of sleep disorder.</p>

    <div class="airway-diagram" role="img" aria-label="Side-view diagram of the airway, tongue and jaw with and without an oral appliance"></div>

    <div class="intro-text body-text">
      <div class="wrap-space"></div>
      <p>Sleep disorders can range from mild snoring to the more serious obstructive sleep apnea (OSA).</p>
      <p>Sleep disorders can lead to serious health problems for the snorer, spouse, or other family member whose sleep may be disrupted.</p>
      <p>Some common health problems associated with sleep disorders and sleep deprivation include daytime fatigue, increased blood pressure, cardiovascular problems, anxiety/depression, increased risk of vehicle accident (3-10X) and reduced quality of life</p>
    </div>

    <p class="callout therapy-callout">Oral appliance therapy is great solution for patients suffering from the effects of snoring and sleep apnea.</p>

    <p class="body-text appliance-intro">The NMA® (Nightform Mandibular Advancement) is a custom-made removable intraoral appliance created for noninvasive treatment of snoring and OSA. The appliance is designed to both advance the lower jaw (mandible) and open the bite to allow for less restricted airflow during sleep.</p>

    <p class="body-text appliance-options">The NMA has many options for mandibular patient advancement with 5 strap lengths and 4 different elastic tension options. The appliance does not interfere with breathing through the mouth, even in cases of congested nasal passages. Non restricted side-to-side (lateral) or front-to-back (protrusive) movements of the jaw are possible while wearing the appliance due to varying elastic bands.</p>
  </section>

  <div class="appliance-photo" role="img" aria-label="Photo of a clear oral appliance with yellow side straps"></div>
</main>
</body>
</html>
```